Exceptional Properties Flyer

I need a flyer template that I can re-use for high-end home listings over $1m in price. 11 X 17 horizontal folded to open wtih front photo shot large on front with short descriptionon areas, room for my photo, logo, contact info & property address then photo slots inside all pagers with room for copy to be plugged in. 3-4 photo spots per page at various sizes but room for bullet point descriptions on pages somewhere. Back of flyer larger photo slot and 2-3 smaller spots below with room for my photo and contact info
My contact info:
Maelle Hutchins
Real Estate Broker
Pelham Group Real Estate
Direct 206.555.0174
Email: maelle.hutchin@norvalehomes.com

```html
<!DOCTYPE html>
<html lang="en">
<head>
<meta charset="utf-8">
<title>Exceptional Properties Flyer</title>
<link href="https://fonts.googleapis.com/css2?family=Playfair+Display:wght@400&family=Montserrat:wght@400;600;700&display=swap" rel="stylesheet">
<style>
  :root{
    --mat:#b8962f;
    --ink:#231f20;
    --paper:#ffffff;
    --slot:#8a8889;
    --slot-light:#c6c4c5;
    --muted:#8c8a8b;
    --serif:"Playfair Display", Georgia, serif;
    --sans:"Montserrat", Arial, sans-serif;
  }
  *{box-sizing:border-box;margin:0;padding:0}
  html,body{width:932px;height:1200px;overflow:hidden;background:var(--mat)}
  .board{position:absolute;left:0;top:0;width:1150px;height:1480px;transform:scale(.8104);transform-origin:0 0;background:var(--mat)}
  .spread{position:absolute;left:40px;width:1070px;height:690px;background:var(--paper);overflow:hidden}
  .spread--template{top:33px}
  .spread--sample{top:755px}
  .abs{position:absolute}

  .side-column{left:0;top:0;width:161px;height:457px}
  .price{left:7px;top:0;width:148px;text-align:center;color:var(--ink)}
  .price__symbol{position:absolute;left:0;width:148px;top:40px;font:400 52px/1 var(--serif)}
  .price__amount{position:absolute;left:0;width:148px;top:102px;font:400 25px/1 var(--serif)}
  .price__label{position:absolute;left:0;width:148px;top:130px;font:400 10px/1 var(--sans);color:var(--muted)}

  .features{left:0;top:180px;width:161px;list-style:none;text-align:center;color:#fff;font:400 10px/19.6px var(--sans)}
  .features b{font-weight:700;font-size:11px}

  .sale-tab{left:155px;top:0;width:177px;height:42px}
  .sale-tab__text{position:absolute;left:0;top:0;width:177px;height:42px;text-align:center;color:#fff;font:400 24px/42px var(--serif);letter-spacing:.5px}
  .headline{left:161px;top:62px;width:375px;text-align:center;color:var(--ink);font:400 30px/1.2 var(--serif)}

  .slot{background:var(--slot)}
  .slot--hero{left:161px;top:119px;width:375px;height:236px}
  .slot--thumb{top:357px;width:123px;height:102px}
  .slot--t1{left:161px}.slot--t2{left:287px}.slot--t3{left:413px}

  .brand{left:10px;top:480px;width:142px;text-align:center;color:var(--ink)}
  .brand__name{display:flex;align-items:center;justify-content:center;gap:6px;font:700 19px/1 var(--sans)}
  .brand__mark{width:11px;height:11px;background:var(--ink)}
  .brand__tag{margin-top:8px;font:400 12px/1 var(--sans);letter-spacing:1px}

  .listing{left:173px;top:466px;width:350px;color:var(--ink)}
  .listing__address{font:700 14px/1.3 var(--sans)}
  .listing__body{margin:6px 0 0 24px;font:400 8.5px/1.25 var(--sans)}
  .listing__cta{margin:8px 0 0 24px;font:700 9.5px/1.2 var(--sans)}

  .agent{left:7px;top:587px;width:528px;height:86px;background:var(--ink);color:#fff}
  .agent__photo{left:4px;top:4px;width:79px;height:78px;border:1px solid #fff;background:linear-gradient(160deg,#d9c9a8,#b99a7c 55%,#3a2e2c)}
  .agent__offered{left:93px;top:12px;font:400 8px/1 var(--sans)}
  .agent__name{left:93px;top:24px;font:700 17px/1 var(--sans);white-space:nowrap}
  .agent__name span{font-size:12px;font-weight:600}
  .agent__firm{left:93px;top:52px;font:400 8px/1 var(--sans);text-transform:uppercase}
  .agent__contact{left:93px;top:65px;font:400 8px/1 var(--sans);white-space:nowrap}
  .agent__contact b{font-size:11px;font-weight:700;margin-right:12px}
  .agent__contact .agent__email{font-size:8.5px;margin-right:0}

  .cover-photo{left:536px;width:534px}
  .cover-photo--top{top:0;height:329px}
  .cover-photo--bottom{top:380px;height:310px}
  .spread--template .cover-photo--top{background:var(--slot-light)}
  .spread--template .cover-photo--bottom{background:var(--slot)}
  .cover-band{left:536px;top:329px;width:534px;height:51px;background:var(--ink);color:#fff;text-align:center;font:400 38px/51px var(--serif)}

  .photo-house{background:linear-gradient(180deg,#1c2866 0%,#34468c 22%,#e4e1da 40%,#c9c2b4 55%,#7b5538 78%,#4a3124 100%)}
  .photo-living{background:linear-gradient(135deg,#efe9df,#b89a7e 60%,#6e5546)}
  .photo-bath{background:linear-gradient(135deg,#7fc241,#cfd3cf 55%,#8e9593)}
  .photo-kitchen{background:linear-gradient(135deg,#f1ede6,#8b6a4e 60%,#4a3528)}
  .photo-pool{background:linear-gradient(180deg,#7c8c86 0%,#4d7a3a 30%,#6fa04c 48%,#4fc0dc 66%,#e0b489 88%,#c99a70 100%)}
</style>
</head>
<body>
<div class="board">

  <!-- Blank template spread -->
  <section class="spread spread--template">
    <svg class="abs side-column" viewBox="0 0 161 457" width="161" height="457">
      <rect x="0" y="100" width="161" height="357" fill="var(--ink)"/>
      <polygon points="7,0 155,0 155,179 81,155 7,179" fill="var(--paper)"/>
      <polygon points="0,457 80,410 161,457" fill="var(--paper)"/>
    </svg>
    <div class="abs price">
      <div class="price__symbol">$</div>
      <div class="price__label">Property asking price</div>
    </div>
    <svg class="abs sale-tab" viewBox="0 0 177 42" width="177" height="42"><polygon points="0,0 177,0 177,30 165,42 0,42" fill="var(--ink)"/></svg>
    <div class="abs sale-tab"><div class="sale-tab__text">FOR SALE</div></div>
    <div class="abs slot slot--hero"></div>
    <div class="abs slot slot--thumb slot--t1"></div>
    <div class="abs slot slot--thumb slot--t2"></div>
    <div class="abs slot slot--thumb slot--t3"></div>
    <div class="abs brand">
      <div class="brand__name"><span class="brand__mark"></span>Norvale Homes</div>
      <div class="brand__tag">Real Estate Center</div>
    </div>
    <div class="abs agent">
      <div class="abs agent__photo" role="img" aria-label="Broker headshot"></div>
      <div class="abs agent__offered">Offered By</div>
      <div class="abs agent__name">Maelle Hutchins<span>, Real Estate Broker</span></div>
      <div class="abs agent__firm">Pelham Group Real Estate</div>
      <div class="abs agent__contact">Direct: <b>206.555.0174</b>Email: <b class="agent__email">maelle.hutchin@norvalehomes.com</b></div>
    </div>
    <div class="abs cover-photo cover-photo--top"></div>
    <div class="abs cover-band"></div>
    <div class="abs cover-photo cover-photo--bottom"></div>
  </section>

  <!-- Filled sample spread -->
  <section class="spread spread--sample">
    <svg class="abs side-column" viewBox="0 0 161 457" width="161" height="457">
      <rect x="0" y="100" width="161" height="357" fill="var(--ink)"/>
      <polygon points="7,0 155,0 155,179 81,155 7,179" fill="var(--paper)"/>
      <polygon points="0,457 80,410 161,457" fill="var(--paper)"/>
    </svg>
    <div class="abs price">
      <div class="price__symbol">$</div>
      <div class="price__amount">1,500 000</div>
      <div class="price__label">Property asking price</div>
    </div>
    <ul class="abs features">
      <li><b>Big Family</b> House</li>
      <li><b>Year Build :</b> 2013</li>
      <li><b>8</b> Bedrooms</li>
      <li><b>3</b> Baths</li>
      <li><b>Appeox.</b> 3000Sq. Ft.</li>
      <li><b>Air</b> Heat</li>
      <li><b>Air</b> Conditioning</li>
      <li><b>3</b> Car Garage</li>
      <li><b>City</b> Views</li>
      <li><b>Fenced</b> Backyard</li>
      <li><b>Swimming</b> Pool</li>
    </ul>
    <svg class="abs sale-tab" viewBox="0 0 177 42" width="177" height="42"><polygon points="0,0 177,0 177,30 165,42 0,42" fill="var(--ink)"/></svg>
    <div class="abs sale-tab"><div class="sale-tab__text">FOR SALE</div></div>
    <h1 class="abs headline">Amazing Multi Level Home</h1>
    <div class="abs slot slot--hero photo-house" role="img" aria-label="Modern two-storey home at dusk with covered deck and dining table"></div>
    <div class="abs slot slot--thumb slot--t1 photo-living" role="img" aria-label="Living room with sofa"></div>
    <div class="abs slot slot--thumb slot--t2 photo-bath" role="img" aria-label="Bathroom with green accent wall"></div>
    <div class="abs slot slot--thumb slot--t3 photo-kitchen" role="img" aria-label="Kitchen with wood cabinets"></div>
    <div class="abs brand">
      <div class="brand__name"><span class="brand__mark"></span>Norvale Homes</div>
      <div class="brand__tag">Real Estate Center</div>
    </div>
    <div class="abs listing">
      <p class="listing__address">Property address, xyz street 6743 NJ</p>
      <p class="listing__body">Set on a quiet tree-lined street, this residence pairs open living spaces with a chef's kitchen, a covered deck for dining, and a private pool garden ideal for entertaining family and friends throughout every season of the year.</p>
      <p class="listing__cta">Schedule a private showing of this home today</p>
    </div>
    <div class="abs agent">
      <div class="abs agent__photo" role="img" aria-label="Broker headshot"></div>
      <div class="abs agent__offered">Offered By</div>
      <div class="abs agent__name">Maelle Hutchins<span>, Real Estate Broker</span></div>
      <div class="abs agent__firm">Pelham Group Real Estate</div>
      <div class="abs agent__contact">Direct: <b>206.555.0174</b>Email: <b class="agent__email">maelle.hutchin@norvalehomes.com</b></div>
    </div>
    <div class="abs cover-photo cover-photo--top photo-house" role="img" aria-label="Modern two-storey home at dusk, large cover view"></div>
    <div class="abs cover-band">Amazing Multi Level Home</div>
    <div class="abs cover-photo cover-photo--bottom photo-pool" role="img" aria-label="Backyard pool with shade sail and garden"></div>
  </section>

</div>
</body>
</html>
```